Breakthrough Medical Research company needs Podcast Album Cover

We are launching a podcast called “The Cortex Bloom Sessions Show” with a mission to accelerate breakthroughs in Neuron Regeneration by bringing together the world’s experts in neurodegenerative diseases, spinal cord injury, and artificial intelligence. Design doesn’t need to be monochromatic but we would like it to utilize the color Blue. The design should also incorporate the Title of the podcast large enough to easily read on a small thumbnail on a phone. We’d also like the design to convey the healing or regeneration of a Neuron.

```html
<!DOCTYPE html>
<html lang="en">
<head>
<meta charset="utf-8">
<title>The Cortex Bloom Sessions Show — Podcast Cover</title>
<link rel="stylesheet" href="https://fonts.googleapis.com/css2?family=Anton&display=swap">
<style>
  :root {
    --blue-deep: #123a72;
    --blue-mid: #1f5f9f;
    --blue-bright: #2b97d6;
    --white: #ffffff;
    --pattern-tone: rgba(10, 40, 90, 0.22);
  }
  html, body {
    margin: 0;
    padding: 0;
    width: 1200px;
    height: 1200px;
    overflow: hidden;
    background: var(--blue-deep);
  }
  .cover {
    position: relative;
    width: 1200px;
    height: 1200px;
    background: linear-gradient(225deg, var(--blue-bright) 0%, var(--blue-mid) 50%, var(--blue-deep) 100%);
    overflow: hidden;
  }
  .cover svg {
    position: absolute;
    inset: 0;
    width: 1200px;
    height: 1200px;
  }
  .title {
    font-family: "Anton", "Impact", sans-serif;
    fill: var(--white);
  }
</style>
</head>
<body>
  <main class="cover">
    <svg viewBox="0 0 1200 1200" xmlns="http://www.w3.org/2000/svg">
      <defs>
        <linearGradient id="patternFade" x1="0" y1="0" x2="1" y2="0">
          <stop offset="0" stop-color="#0a285a" stop-opacity="0.28"/>
          <stop offset="1" stop-color="#0a285a" stop-opacity="0"/>
        </linearGradient>
        <radialGradient id="neuronTone" cx="0.5" cy="0.5" r="0.55">
          <stop offset="0" stop-color="#ffffff" stop-opacity="0.95"/>
          <stop offset="1" stop-color="#ffffff" stop-opacity="0.15"/>
        </radialGradient>
        <linearGradient id="axonTone" x1="1" y1="0" x2="0" y2="1">
          <stop offset="0" stop-color="#ffffff" stop-opacity="0.85"/>
          <stop offset="1" stop-color="#ffffff" stop-opacity="0.15"/>
        </linearGradient>
      </defs>

      <rect class="binary-pattern" x="0" y="0" width="640" height="1200" fill="url(#patternFade)"
            role="img" aria-label="Faint columns of binary digits running down the left side"/>

      <rect class="neuron-cell" x="780" y="50" width="400" height="310" rx="150" fill="url(#neuronTone)"
            role="img" aria-label="White neuron cell body with branching dendrites"/>

      <rect class="neuron-axon" x="330" y="805" width="260" height="325" rx="90" fill="url(#axonTone)"
            role="img" aria-label="White axon descending and branching into terminals"/>

      <text class="title title-line-one" x="77" y="578" font-size="250"
            textLength="1037" lengthAdjust="spacingAndGlyphs">The Cortex Bloom</text>
      <text class="title title-line-two" x="75" y="795" font-size="230"
            textLength="1050" lengthAdjust="spacingAndGlyphs">Sessions Show</text>

      <g class="title-plus" fill="var(--white)">
        <rect x="664" y="605" width="30" height="7"/>
        <rect x="675" y="594" width="8" height="29"/>
      </g>
    </svg>
  </main>
</body>
</html>
```